Unique business card design

We are looking for a design that reflects our unique social media and online marketing agency "Kelvora Media". We are a young agency with a focus on speakers, coaches and trainers. In other words, we support people who want to do good with their work and help other people live a happier, more successful and fulfilling life, reach as many people as possible with their work and thus have an influence. Our values are: sustainability, creating added value, individuality, proactivity. We want our clients to feel comfortable with us and that's why the relationship with them is very important to us. We want every customer to become a lifelong friend of the company. Most of our clients are premium coaches, meaning they are in the higher priced segment and expect seriousness, professionalism and quality. All of these things should reflect our business card as well. I look forward to feedback. Best regards, Dorian Whitcombe
Look and feel
Each slider illustrates characteristics of the customer's brand and the style your logo design should communicate.

```html
<!DOCTYPE html>
<html lang="de">
<head>
<meta charset="utf-8">
<title>Kelvora Media – Visitenkarte</title>
<link href="https://fonts.googleapis.com/css2?family=Questrial&display=swap" rel="stylesheet">
<style>
  :root {
    --page: #ffffff;
    --card-blue: #1673b9;
    --ink: #2a2466;
    --shadow: rgba(0, 0, 0, 0.22);
  }
  * { margin: 0; padding: 0; box-sizing: border-box; }
  html, body {
    width: 1200px;
    height: 1200px;
    overflow: hidden;
    background: var(--page);
    font-family: "Questrial", "Century Gothic", sans-serif;
    color: var(--ink);
  }
  .canvas { position: relative; width: 1200px; height: 1200px; }

  .card {
    position: absolute;
    background: var(--card-blue);
    box-shadow: 6px 8px 6px var(--shadow);
    text-align: center;
  }
  .card--front { left: 170px; top: 190px; width: 388px; height: 680px; }
  .card--back  { left: 634px; top: 392px; width: 385px; height: 674px; }

  .brand {
    position: absolute;
    left: 0; right: 0; top: 112px;
    display: flex;
    flex-direction: column;
    align-items: center;
  }
  .brand__row { display: flex; align-items: center; gap: 8px; }
  .brand__mark { width: 16px; height: 16px; background: var(--ink); }
  .brand__name { font-size: 25px; line-height: 1; letter-spacing: 0.2px; }
  .brand__tagline { margin-top: 8px; font-size: 9.5px; letter-spacing: 0.4px; }

  .person { position: absolute; left: 0; right: 0; top: 312px; }
  .person__name { font-size: 24px; line-height: 1.1; }
  .person__role { font-size: 18.5px; line-height: 1.3; }

  .contact {
    position: absolute; left: 0; right: 0; top: 516px;
    list-style: none;
    font-size: 22px;
    line-height: 26px;
  }
  .contact__item { display: flex; justify-content: center; align-items: center; gap: 6px; }
  .contact__icon { width: 18px; height: 18px; fill: var(--ink); }

  .values {
    position: absolute; left: 0; right: 0; top: 300px;
    list-style: none;
    font-size: 30px;
    line-height: 40.5px;
  }
</style>
</head>
<body>
<main class="canvas">

  <section class="card card--front" aria-label="Vorderseite">
    <div class="brand">
      <div class="brand__row">
        <span class="brand__mark"></span>
        <span class="brand__name">Kelvora Media</span>
      </div>
      <span class="brand__tagline">Online Marketing Services</span>
    </div>

    <div class="person">
      <p class="person__name">Dorian Whitcombe</p>
      <p class="person__role">Your Designation</p>
    </div>

    <ul class="contact">
      <li class="contact__item">
        <svg class="contact__icon" viewBox="0 0 24 24" aria-hidden="true">
          <path d="M6.6 10.8a15.1 15.1 0 0 0 6.6 6.6l2.2-2.2a1 1 0 0 1 1-.25 11.4 11.4 0 0 0 3.6.57 1 1 0 0 1 1 1V20a1 1 0 0 1-1 1A17 17 0 0 1 3 4a1 1 0 0 1 1-1h3.5a1 1 0 0 1 1 1 11.4 11.4 0 0 0 .57 3.6 1 1 0 0 1-.25 1z"/>
        </svg>
        <span>123.456.7890</span>
      </li>
      <li class="contact__item">
        <svg class="contact__icon" viewBox="0 0 24 24" aria-hidden="true" style="width:26px">
          <path d="M2 5h20v2l-10 6L2 7z"/>
          <path d="M2 9l10 6 10-6v10H2z"/>
        </svg>
        <span>youremail@email.com</span>
      </li>
      <li class="contact__item">
        <svg class="contact__icon" viewBox="0 0 24 24" aria-hidden="true">
          <path d="M12 2a10 10 0 1 0 0 20 10 10 0 0 0 0-20zm-1 3c-1 1.5-3 1.5-3 3.5s2 1.5 2 3-2 1-2 3 2 2 3 4.2A8 8 0 0 1 5.5 8 8 8 0 0 1 11 5zm3 1.2a8 8 0 0 1 4.8 9.3c-.8-1-2-.5-2.5-1.8s.7-2.6-.6-3.4-2.4.3-3-1 1.5-2 1.3-3.1z"/>
        </svg>
        <span>yourwebsite.com</span>
      </li>
    </ul>
  </section>

  <section class="card card--back" aria-label="Rückseite">
    <div class="brand">
      <div class="brand__row">
        <span class="brand__mark"></span>
        <span class="brand__name">Kelvora Media</span>
      </div>
      <span class="brand__tagline">Online Marketing Services</span>
    </div>

    <ul class="values">
      <li>Nachhaltigkeit</li>
      <li>Mehrwert schaffen</li>
      <li>Individualität</li>
      <li>Proaktivität</li>
    </ul>
  </section>

</main>
</body>
</html>
```